Website redesign: LUMO - Frame Works Studio

Web Design Brief
I'm looking for a redesign of our website https://www.lumoframe.studio/. The website is built with Wix.

We are an AI Video Production Agency named LUMO that uses AI-technology to create videos for our clients. We use the platform vexorant.io to generate videos.

Use case:
A financial services company is looking for a way to transform their inhouse training content to video.
They visit lumoframe.studio and submit a brief.
Several production packages are presented, and the company selects the one that suits them best. Pricing is agreed upon, and the company provides the necessary scripts and documentation.

As a growing agency, our web page's primary objective is to acquire business leads (companies seeking professional video services) and to communicate our unique AI-driven approach to video production. The landing page will include a form for potential clients to fill out their requirements, as well as a showcase of our AI's capabilities in video production.

We have not yet chosen a color palette, but we are looking for a design that will inspire confidence in our clients while also highlighting the innovative and creative nature of our service. The overall theme should be sleek, modern, and visual, as our core offering is video creation and editing.

Current website:
https://www.lumoframe.studio/

Competitors:
https://www.clipnest.pro/
https://quillbox.ai/
https://www.pelmoreel.com/vexorant

Inspiration:
https://www.vexorant.io/
https://wenly.co.uk/
https://brightfolk.co/
https://www.harrowpine.com/

Target Market(s)

Director's of training and others who work with video at companies with $10M+ in revenue and 100+ employees.

Industry/Entity Type

Video Services Agency

Coding

Coded - Design and coding required

Number of Pages Required

1 page

Font styles to use
Sans Serif

Requirements
Must have
• Clear CTA and services showcase above the fold. Include "Services" and "Blog" section.
Nice to have
• Reviews / Proof of concept

```html
<!DOCTYPE html>
<html lang="en">
<head>
<meta charset="utf-8">
<title>LUMO - Frame Works Studio</title>
<link rel="stylesheet" href="https://fonts.googleapis.com/css2?family=Chakra+Petch:wght@400;500&family=Poppins:wght@400;500;600&display=swap">
<style>
:root{
  --blue-light:#05b4f2;
  --blue-deep:#1667e9;
  --blue-frame:#2f8ef3;
  --frame-pale:#c6dbf9;
  --ink:#141821;
  --text:#4a4f5a;
  --white:#ffffff;
  --footer:#10141f;
  --footer-text:#b9bdc8;
  --icon-soft:#c9dbfb;
  --icon-strong:#1d63ea;
}
*{box-sizing:border-box;margin:0;padding:0}
html,body{width:1200px;height:3004px;overflow:hidden}
body{position:relative;font-family:"Poppins",sans-serif;color:var(--ink);background:var(--white)}
.abs{position:absolute}
.display{font-family:"Chakra Petch",sans-serif;font-weight:500}
.band{position:absolute;left:0;width:1200px;background:linear-gradient(135deg,var(--blue-light) 0%,var(--blue-deep) 100%)}
.hero{top:0;height:633px}
.brand{display:flex;align-items:center;gap:10px;color:var(--white)}
.brand-dot{width:40px;height:40px;border-radius:50%;border:3px solid var(--white)}
.brand-name{font-weight:600;font-size:32px;letter-spacing:2px;line-height:1}
.nav{top:22px;left:481px;display:flex;gap:28px;font-size:14px;color:var(--white)}
.btn-outline{border:1.5px solid var(--white);border-radius:30px;color:var(--white);font-weight:600;font-size:13px;display:flex;align-items:center;justify-content:center}
.btn-solid{background:var(--white);border-radius:30px;color:var(--ink);font-weight:600;font-size:13px;display:flex;align-items:center;justify-content:center;gap:12px}
.hero-title{left:108px;top:160px;width:460px;font-size:29px;line-height:35px;color:var(--white);letter-spacing:1px}
.hero-copy{left:108px;top:325px;width:400px;font-size:13.5px;line-height:20px;color:var(--white)}
.frame{border-radius:40px;padding:14px}
.frame-blue{background:var(--blue-frame)}
.frame-pale{background:var(--frame-pale)}
.photo{width:100%;height:100%;border-radius:28px;position:relative;overflow:hidden}
.photo-light{background:linear-gradient(180deg,#f3f1ef 0%,#e4dcd6 55%,#2a2a2e 100%)}
.photo-suit{background:linear-gradient(180deg,#eef0f2 0%,#d9dadd 50%,#2c3048 100%)}
.photo-navy{background:linear-gradient(180deg,#f6f4f3 0%,#e6ddd7 55%,#1f2746 100%)}
.play-pill{position:absolute;left:50%;transform:translateX(-50%);bottom:42px;height:38px;padding:0 16px 0 10px;background:var(--white);border-radius:20px;display:flex;align-items:center;gap:10px;font-size:13px;font-weight:600;white-space:nowrap}
.play-pill svg{width:20px;height:20px}
.card{top:710px;width:316px;height:316px;border-radius:26px;background:var(--white);box-shadow:0 10px 40px rgba(20,40,90,.09);text-align:center;padding:50px 34px 0}
.card svg{width:46px;height:46px;margin-bottom:28px}
.card h3{font-size:20px;font-weight:600;line-height:28px;margin-bottom:4px}
.card p{font-size:13.5px;line-height:20px;color:var(--text)}
.section-title{font-size:28px;color:var(--ink)}
.body-copy{font-size:13.5px;line-height:20px;color:var(--text)}
.body-copy p+p{margin-top:20px}
.contact{top:2059px;height:522px}
.label{font-size:11.5px;font-weight:600;color:var(--white)}
.field{background:var(--white);border-radius:12px;font-size:11.5px;color:#8a8f99;padding:10px}
.footer{position:absolute;left:0;top:2581px;width:1200px;height:423px;background:var(--footer);color:var(--footer-text)}
.foot-col h4{font-size:15px;font-weight:500;color:var(--white);margin-bottom:22px}
.foot-col li{list-style:none;font-size:13.5px;line-height:27px}
.social{width:36px;height:36px;border-radius:50%;background:var(--white)}
</style>
</head>
<body>

<section class="band hero">
  <div class="abs brand" style="left:108px;top:12px">
    <span class="brand-dot"></span><span class="brand-name">LUMO</span>
  </div>
  <nav class="abs nav"><span>Training</span><span>Marketing</span><span>How?</span><span>More</span></nav>
  <div class="abs btn-outline" style="left:983px;top:12px;width:109px;height:37px">CONTACT US</div>

  <h1 class="abs display hero-title">GROW YOUR BUSINESS BY IMPROVING OPERATIONS EFFICIENCY THROUGH VIDEO POWERED BY AI</h1>
  <p class="abs hero-copy">LUMO levels up your training and marketing teams thanks to high-quality and efficient video production powered by AI. You will combine the latest technology available with the most professional and human touch.</p>
  <div class="abs btn-solid" style="left:108px;top:425px;width:226px;height:44px">SEE IT IN ACTION NOW
    <svg width="16" height="14" viewBox="0 0 16 14"><path d="M1 7h13M9 2l5 5-5 5" fill="none" stroke="#141821" stroke-width="2"/></svg>
  </div>

  <div class="abs frame frame-blue" style="left:679px;top:103px;width:425px;height:427px">
    <div class="photo photo-light" role="img" aria-label="Portrait of a female AI presenter in a dark top">
      <div class="play-pill"><svg viewBox="0 0 20 20"><circle cx="10" cy="10" r="10" fill="#1d63ea"/><path d="M8 6l6 4-6 4z" fill="#fff"/></svg>SEE HOW IT WORKS</div>
    </div>
  </div>
</section>

<article class="abs card" style="left:108px">
  <svg viewBox="0 0 46 46"><circle cx="23" cy="23" r="22" fill="var(--icon-soft)"/><path d="M23 12v12l-4 2" fill="none" stroke="var(--icon-strong)" stroke-width="3" stroke-linecap="round"/></svg>
  <h3>Save 80% of your time</h3>
  <p>Your human expert in video edition will be working for you autonomously, saving your teams time.</p>
</article>
<article class="abs card" style="left:442px">
  <svg viewBox="0 0 46 46"><rect x="1" y="2" width="44" height="42" rx="8" fill="var(--icon-soft)"/><rect x="8" y="10" width="37" height="6" rx="3" fill="#fff" opacity=".8"/><circle cx="36" cy="30" r="2.2" fill="var(--icon-strong)"/></svg>
  <h3>Save 80% of your budget</h3>
  <p>Forget about long and expensive production costs, you will make better quality videos for less money.</p>
</article>
<article class="abs card" style="left:775px">
  <svg viewBox="0 0 46 46"><circle cx="21" cy="25" r="20" fill="var(--icon-soft)"/><path d="M26 0a20 20 0 0 1 20 20H26z" fill="var(--icon-strong)"/></svg>
  <h3>Boost your business efficiency</h3>
  <p>You can use video to automate different areas of your business such as Marketing, Training &amp; Onboarding.</p>
</article>

<h2 class="abs display section-title" style="left:108px;top:1163px">Training</h2>
<div class="abs body-copy" style="left:108px;top:1218px;width:485px">
  <p>LUMO - Frame Works Studio presents the 5 Benefits of using video for training. At LUMO, we understand the importance of engaging and interactive training materials. That's why we offer a unique service that transforms boring documents like powerpoints, PDFs, and static web pages into dynamic and engaging AI videos.</p>
  <p>Our process begins by analysing your existing training materials and identifying key points that can be enhanced through the use of video. The process for you it's really simple, you send us the documents or URL and we take care of all the edition work, you will receive the videos ready to use in MP4 format or we can upload them to the platform you need.</p>
</div>
<div class="abs frame frame-pale" style="left:679px;top:1090px;width:425px;height:427px">
  <div class="photo photo-suit" role="img" aria-label="Portrait of a male AI presenter in a pinstripe suit">
    <div class="play-pill"><svg viewBox="0 0 20 20"><circle cx="10" cy="10" r="10" fill="#1d63ea"/><path d="M8 6l6 4-6 4z" fill="#fff"/></svg>SEE HOW IT WORKS</div>
  </div>
</div>

<div class="abs frame frame-pale" style="left:96px;top:1568px;width:425px;height:427px">
  <div class="photo photo-navy" role="img" aria-label="Portrait of a female AI presenter in a navy top">
    <div class="play-pill"><svg viewBox="0 0 20 20"><circle cx="10" cy="10" r="10" fill="#1d63ea"/><path d="M8 6l6 4-6 4z" fill="#fff"/></svg>SEE HOW IT WORKS</div>
  </div>
</div>
<h2 class="abs display section-title" style="left:609px;top:1711px">Marketing</h2>
<div class="abs body-copy" style="left:609px;top:1766px;width:490px">
  <p>We are really proud to present the new video we created for Marlo Pevensey Ortal that promotes his APP available for both Droidline &amp; Pomeos. This video will be featured in Playhub Store &amp; Orchard Store with more than 80.000 Downloads on both platforms.</p>
</div>

<section class="band contact">
  <h2 class="abs display section-title" style="left:108px;top:178px;color:var(--white)">Let's talk</h2>
  <p class="abs" style="left:108px;top:233px;width:370px;font-size:13.5px;line-height:20px;color:var(--white)">We will contact you shortly, alternatively you can book a free 15 minutes strategy call.</p>
  <div class="abs btn-outline" style="left:108px;top:293px;width:136px;height:44px">BOOK NOW</div>

  <span class="abs label" style="left:691px;top:82px">Name</span>
  <div class="abs field" style="left:691px;top:100px;width:192px;height:36px">John Due</div>
  <span class="abs label" style="left:900px;top:82px">Phone number</span>
  <div class="abs field" style="left:900px;top:100px;width:192px;height:36px">+1 555 0184</div>
  <span class="abs label" style="left:691px;top:154px">Email</span>
  <div class="abs field" style="left:691px;top:172px;width:401px;height:36px">mail@example.com</div>
  <span class="abs label" style="left:691px;top:227px">Tell us about your project</span>
  <div class="abs field" style="left:691px;top:245px;width:401px;height:130px">Type your message</div>
  <div class="abs btn-solid" style="left:813px;top:402px;width:157px;height:44px;font-size:14px">GET STARTED</div>
</section>

<footer class="footer">
  <div class="abs brand" style="left:108px;top:78px">
    <span class="brand-dot" style="width:64px;height:64px"></span><span class="brand-name" style="font-size:48px">LUMO</span>
  </div>
  <p class="abs" style="left:108px;top:174px;width:320px;font-size:11.5px;line-height:17px;font-style:italic;color:#d6d9e0">I only provided screenshots of my app and its main features. Then LUMO's creative process kicked in and the result was a great promo video that I uploaded on Playhub and Orchard Store.</p>
  <p class="abs" style="left:108px;top:263px;font-size:11.5px;color:#d6d9e0"><span style="color:var(--white);font-weight:600;text-decoration:underline">Marlo Pevensey Ortal |</span> Senior Droidline &amp; Pomeos Engine</p>

  <div class="abs foot-col" style="left:525px;top:80px"><h4>Quick Links</h4><ul><li>Training</li><li>Marketing</li><li>How?</li><li>More</li></ul></div>
  <div class="abs foot-col" style="left:704px;top:80px"><h4>Company</h4><ul><li>Terms and Condition</li><li>Privacy and Plicy</li><li>Career</li><li>Help Center</li></ul></div>
  <div class="abs foot-col" style="left:940px;top:80px"><h4>Contact Us</h4><ul>
    <li><svg width="13" height="13" viewBox="0 0 24 24" style="margin-right:10px;vertical-align:-1px"><path d="M6.6 10.8a15 15 0 0 0 6.6 6.6l2.2-2.2c.3-.3.7-.4 1-.2 1.1.4 2.3.6 3.6.6.6 0 1 .4 1 1V20c0 .6-.4 1-1 1A17 17 0 0 1 3 4c0-.6.4-1 1-1h3.5c.6 0 1 .4 1 1 0 1.3.2 2.5.6 3.6.1.3 0 .7-.2 1z" fill="#b9bdc8"/></svg>+1 555 01842</li>
    <li><svg width="13" height="11" viewBox="0 0 24 18" style="margin-right:10px"><rect width="24" height="18" rx="2" fill="#b9bdc8"/><path d="M1 2l11 8 11-8" fill="none" stroke="#10141f" stroke-width="2"/></svg>hello@lumoframe.studio</li></ul></div>

  <div class="abs" style="left:108px;top:349px;width:984px;height:1px;background:#c8ccd4"></div>
  <p class="abs" style="left:108px;top:380px;font-size:10px">© 2023 Powered by LUMO - Frame Works Studio</p>
  <div class="abs social" style="left:971px;top:370px" aria-label="Social profile"></div>
  <div class="abs social" style="left:1014px;top:370px" aria-label="Social profile"></div>
  <div class="abs social" style="left:1056px;top:370px" aria-label="Social profile"></div>
</footer>

</body>
</html>
```